Emerging automotive detailing business

I am starting a small automotive detailing business in hopes of becoming a well-known detailer to work on high end cars. I would like a card to reflect the high quality and time I put into my work. The name of the company is Brightmere Detailing. I feel like it represents racecars getting off the line at the drag strip as well as an innuendo of "Off the Charts". I do minor paint correction such as clay barring, multi-step buffing and polishing, waxing, hand washes, etc. I am always striving to learn more and improve my work. My goal is to have total customer satisfaction. This is a female run business but I do not want it to be very girly. Elegant is okay! I have pictures of my personal kestrel attached, they do not need to be incorporated but if you can think of a cool way to use 1 or all of them, go for it!

Target Market(s)

Anyone that owns a vehicle. Preferably high end vehicles such as Valdren, Castavelli and Moretto but I will also happily work on any car, truck or suv no matter what brand.

Industry/Entity Type

Automotive

Contact Information for Business Card

Brightmere Detailing
Nora Pellworth
4715 Quillbrook Rd
Marlow Bend VT 05999
Cell phone- call/text- 555-555-0148
email- brightmeredetails@example.com
Instagram: @brightmeredetailing
Facebook: facebook.example/brightmeredetailing

Requirements
Must have
• Business name, my name, address, phone number. Listing that I do minor paint correction such as clay barring, multi-step buffing and polishing, waxing, hand washes, interior cleaning, and more. (This last part was in nice to haves but I have realized that I do really want it, so I moved it to must haves.) I want something that is different and eye-catching to my customers. Some people have done this very well with cards already submitted to me, but a lot have not. I didn't mess with the "look and feel bars" much because because I am pretty open to the overall design as long as it is not your basic run of the mill design.
Nice to have
• Something car related. Maybe an appointment time/date line. I do not have a logo, but if you would like to design one and incorporate it, that would be amazing!
Should not have
• Purple and Pink colors. Boring, basic, normal card.

```html
<!DOCTYPE html>
<html lang="en">
<head>
<meta charset="utf-8">
<title>Brightmere Detailing – Business Card</title>
<link href="https://fonts.googleapis.com/css2?family=Open+Sans:wght@400;600;700&display=swap" rel="stylesheet">
<style>
  :root {
    --stage: #e7e4e0;
    --paper: #ffffff;
    --ink: #1f1f1f;
    --charcoal-deep: #111214;
    --brand-red: #e4211b;
    --brand-blue: #3fa3dd;
    --shadow-grey: #d9d9d9;
    --white: #ffffff;
    --photo-sky: #cfd6dc;
    --photo-yellow: #e8c41a;
    --photo-ground: #7c7363;
  }
  * { box-sizing: border-box; margin: 0; padding: 0; }
  html, body { width: 1200px; height: 1000px; overflow: hidden; }
  body {
    background: var(--stage);
    font-family: "Open Sans", Arial, sans-serif;
    color: var(--ink);
    position: relative;
  }
  .card {
    position: absolute;
    width: 729px;
    height: 436px;
    overflow: hidden;
    box-shadow: 0 6px 14px rgba(0,0,0,0.25);
  }
  /* Front */
  .card--front { left: 54px; top: 43px; background: var(--paper); }
  .front-shapes { position: absolute; inset: 0; }
  .holder-name {
    position: absolute; left: 33px; top: 144px;
    font-size: 26px; font-weight: 700; color: var(--brand-red);
  }
  .contact-list { position: absolute; left: 32px; top: 245px; list-style: none; }
  .contact-item {
    display: flex; align-items: flex-start; gap: 12px;
    font-size: 18px; line-height: 25px; margin-bottom: 12px;
  }
  .contact-item:nth-child(3) { margin-bottom: 15px; }
  .contact-icon { width: 20px; height: 20px; flex: none; margin-top: 3px; }
  .brand-name {
    position: absolute; left: 396px; top: 130px; width: 310px;
    text-align: center;
    font-size: 21px; font-weight: 700; letter-spacing: 0.5px;
    color: var(--brand-blue); text-transform: uppercase;
  }
  /* Back */
  .card--back { left: 397px; top: 509px; background: var(--charcoal-deep); }
  .hero-photo {
    position: absolute; left: 0; top: 0; width: 729px; height: 314px;
    background:
      radial-gradient(ellipse 45% 55% at 50% 65%, var(--photo-yellow) 0%, #d2ad12 55%, transparent 75%),
      linear-gradient(180deg, var(--photo-sky) 0%, #9aa08a 45%, var(--photo-ground) 100%);
  }
  .accent-rule {
    position: absolute; left: 0; top: 314px; width: 729px; height: 4px;
    background: var(--brand-red);
  }
  .back-brand {
    position: absolute; left: 30px; top: 396px; width: 290px;
    text-align: center;
    font-size: 17px; font-weight: 700; letter-spacing: 0.4px;
    color: var(--brand-blue); text-transform: uppercase;
  }
  .services {
    position: absolute; left: 360px; top: 343px; width: 340px;
    text-align: center; color: var(--white);
    font-size: 15px; font-weight: 700; line-height: 23px; text-transform: uppercase;
  }
  .services .dot { color: var(--brand-red); margin: 0 3px; }
</style>
</head>
<body>

<section class="card card--front" aria-label="Business card front">
  <svg class="front-shapes" width="729" height="436" viewBox="0 0 729 436" aria-hidden="true">
    <defs>
      <linearGradient id="panelShade" x1="0" y1="0" x2="1" y2="1">
        <stop offset="0" stop-color="#232427"/>
        <stop offset="1" stop-color="#17181a"/>
      </linearGradient>
    </defs>
    <polygon points="322,0 336,0 412,436 392,436" fill="var(--shadow-grey)"/>
    <polygon points="330,0 342,0 426,436 410,436" fill="var(--brand-red)"/>
    <polygon points="342,0 729,0 729,436 426,436" fill="url(#panelShade)"/>
    <polygon points="480,0 729,0 729,140 560,300" fill="#ffffff" opacity="0.015"/>
    <polygon points="420,210 729,60 729,220 470,436" fill="#ffffff" opacity="0.012"/>
  </svg>

  <div class="brand-name">Brightmere Detailing</div>

  <h1 class="holder-name">Nora Pellworth</h1>

  <ul class="contact-list">
    <li class="contact-item">
      <svg class="contact-icon" viewBox="0 0 24 24" aria-hidden="true">
        <circle cx="12" cy="12" r="10" fill="none" stroke="var(--brand-blue)" stroke-width="1.8"/>
        <path d="M8.5 7.5c.6-.6 1.4-.5 1.8.1l.9 1.5c.3.5.2 1.1-.2 1.4l-.6.5c.5 1.2 1.4 2.1 2.6 2.6l.5-.6c.3-.4.9-.5 1.4-.2l1.5.9c.6.4.7 1.2.1 1.8-.9.9-2.3 1.2-3.6.5-2-1-3.7-2.7-4.7-4.7-.6-1.3-.5-2.7.3-3.8z" fill="var(--brand-blue)"/>
      </svg>
      <span>555-555-0148</span>
    </li>
    <li class="contact-item">
      <svg class="contact-icon" viewBox="0 0 24 24" aria-hidden="true">
        <rect x="2" y="5" width="20" height="14" rx="1" fill="none" stroke="var(--brand-blue)" stroke-width="1.8"/>
        <path d="M2.5 5.5 12 13l9.5-7.5" fill="none" stroke="var(--brand-blue)" stroke-width="1.8"/>
      </svg>
      <span>brightmeredetails@example.com</span>
    </li>
    <li class="contact-item">
      <svg class="contact-icon" viewBox="0 0 24 24" aria-hidden="true">
        <path d="M12 3 2 12h3v8h5v-5h4v5h5v-8h3z" fill="var(--brand-blue)"/>
      </svg>
      <span>4715 Quillbrook Rd<br>Marlow Bend VT 05999</span>
    </li>
    <li class="contact-item">
      <svg class="contact-icon" viewBox="0 0 24 24" aria-hidden="true">
        <rect x="2" y="2" width="20" height="20" rx="4" fill="var(--brand-blue)"/>
      </svg>
      <span>@brightmeredetailing</span>
    </li>
  </ul>
</section>

<section class="card card--back" aria-label="Business card back">
  <div class="hero-photo" role="img" aria-label="Photograph of a yellow sports car with a black hood stripe, parked on gravel in front of autumn brush"></div>
  <div class="accent-rule"></div>
  <div class="back-brand">Brightmere Detailing</div>
  <p class="services">
    Clay Barring<span class="dot">•</span>Multi-Step Buffing<br>
    and Polishing<br>
    Waxing<span class="dot">•</span>Hand Washes and More
  </p>
</section>

</body>
</html>
```